Business Card for Modern Marketing Consultancy

Business card needed for marketing consultancy with existing logo.

Lanternway Co is a specialized boutique marketing consultancy that provides startup, small and mid size consumer businesses thought leadership and implementation of marketing strategies to help your business grow.

Our expertise, experience and industry knowledge stems from some of New York’s top global beauty and retail companies and allows us to draw from an array of successful marketing strategies and growth tactics tailored to suit the needs of your business

lanternwayco.example

Target Market(s)

start up, small and mid size consumer packaged goods businesses

Industry/Entity Type

Leadership

Requirements
Must have
• Must have the logo of the business and use of the exact colors of the logo.
Must be simple, sleek, modern and clean. Must make a statement and be eye catching.

Front: looking for unique design or visual statement with logo and tagline

Back of card should have:
logo - if not use on front.
Delia R. Horvath
Founder
Lanternway Co
m: 555.014.2276
deliahorvath@lanternwayco.example
lanternwayco.example

Please use the following words as these describe my services:
strategy analytics branding research

Please refer to the website look and feel: lanternwayco.example

Please kindly note that I am looking for a unique design that I cannot do myself with a template. thank you.
Nice to have
• Please also try and incorporate additional files attached.

```html
<!DOCTYPE html>
<html lang="en">
<head>
<meta charset="utf-8">
<title>Lanternway Co business card</title>
<link rel="stylesheet" href="https://fonts.googleapis.com/css2?family=Quicksand:wght@500;600&family=Open+Sans:wght@400&display=swap">
<style>
  :root {
    --backdrop: #6d6e70;
    --magenta: #d4216e;
    --magenta-deep: #a30a47;
    --magenta-glow: #e02a7a;
    --ink-grey: #67686b;
    --paper: #ffffff;
    --mist: #efefef;
    --soft-grey: #7a7a7c;
  }
  * { margin: 0; padding: 0; box-sizing: border-box; }
  html, body {
    width: 1200px; height: 934px; overflow: hidden;
    background: var(--backdrop);
  }
  .stage { position: relative; width: 1200px; height: 934px; }

  .card { position: absolute; overflow: hidden; }

  /* Front */
  .card-front {
    left: 115px; top: 30px; width: 635px; height: 388px;
    background: radial-gradient(ellipse 60% 70% at 48% 50%, var(--magenta-glow) 0%, var(--magenta) 40%, var(--magenta-deep) 100%);
  }
  .front-visual {
    position: absolute; left: 355px; top: 0; width: 280px; height: 300px;
    background: radial-gradient(ellipse 55% 55% at 55% 48%, var(--mist) 0%, var(--mist) 45%, rgba(239,239,239,0.35) 75%, rgba(239,239,239,0) 100%);
  }
  .front-brand {
    position: absolute; left: 15px; top: 286px;
    font-family: "Quicksand", sans-serif; font-weight: 600;
    font-size: 53px; line-height: 1; color: var(--paper);
    letter-spacing: -0.5px;
  }
  .front-tagline {
    position: absolute; left: 97px; top: 349px;
    font-family: "Open Sans", sans-serif; font-size: 15px;
    color: var(--paper); letter-spacing: 0.3px;
  }

  /* Back */
  .card-back {
    left: 464px; top: 467px; width: 666px; height: 408px;
    background: var(--paper);
  }
  .back-brand {
    position: absolute; left: 161px; top: 45px;
    font-family: "Quicksand", sans-serif; font-weight: 600;
    font-size: 48px; line-height: 1; color: var(--ink-grey);
    letter-spacing: -0.5px;
  }
  .back-tagline {
    position: absolute; left: 234px; top: 98px;
    font-family: "Open Sans", sans-serif; font-size: 14px;
    color: var(--magenta); letter-spacing: 0.3px;
  }
  .person-name {
    position: absolute; left: 200px; top: 156px;
    font-family: "Quicksand", sans-serif; font-weight: 500;
    font-size: 33px; line-height: 1.2; color: var(--magenta);
  }
  .person-role {
    position: absolute; left: 200px; top: 197px;
    font-family: "Open Sans", sans-serif; font-size: 17px;
    color: var(--ink-grey);
  }
  .contact-list { position: absolute; left: 200px; top: 229px; list-style: none; }
  .contact-item {
    display: flex; align-items: center; gap: 6px; height: 28px;
    font-family: "Open Sans", sans-serif; font-size: 15px; color: var(--magenta);
  }
  .contact-icon { width: 14px; height: 14px; flex: none; }

  .service-list { list-style: none; }
  .service-item {
    position: absolute; top: 362px;
    display: flex; align-items: center; gap: 9px;
    font-family: "Open Sans", sans-serif; font-size: 15px; color: var(--soft-grey);
  }
  .service-item::before {
    content: ""; width: 7px; height: 7px; border-radius: 50%;
    background: var(--magenta);
  }
  .service-strategy { left: 16px; }
  .service-analytics { left: 164px; }
  .service-branding { left: 352px; }
  .service-research { left: 553px; }

  .card-band {
    position: absolute; left: 0; bottom: 0; width: 100%; height: 13px;
    background: linear-gradient(90deg, var(--magenta) 0%, var(--magenta-deep) 100%);
  }
</style>
</head>
<body>
<main class="stage">

  <section class="card card-front" aria-label="Card front">
    <div class="front-visual" role="img" aria-label="Large light brand illustration on the magenta field"></div>
    <div class="front-brand">Lanternway Co</div>
    <div class="front-tagline">discover intelligent marketing</div>
  </section>

  <section class="card card-back" aria-label="Card back">
    <div class="back-brand">Lanternway Co</div>
    <div class="back-tagline">discover intelligent marketing</div>

    <div class="person-name">Delia R. Horvath</div>
    <div class="person-role">Founder</div>

    <ul class="contact-list">
      <li class="contact-item">
        <svg class="contact-icon" viewBox="0 0 14 14" aria-hidden="true">
          <circle cx="7" cy="7" r="7" fill="var(--magenta)"/>
          <path d="M4.3 3.6 L5.8 3.4 L6.3 5.3 L5.4 6 Q6.2 7.7 8 8.6 L8.7 7.7 L10.6 8.2 L10.4 9.7 Q6.8 10.2 4.3 3.6 Z" fill="#fff"/>
        </svg>
        <span>555.014.2276</span>
      </li>
      <li class="contact-item">
        <svg class="contact-icon" viewBox="0 0 14 14" aria-hidden="true">
          <circle cx="7" cy="7" r="7" fill="var(--magenta)"/>
          <rect x="3.5" y="4.5" width="7" height="5" fill="#fff"/>
          <path d="M3.5 4.5 L7 7.3 L10.5 4.5" fill="none" stroke="var(--magenta)" stroke-width="0.9"/>
        </svg>
        <span>deliahorvath@lanternwayco.example</span>
      </li>
      <li class="contact-item">
        <svg class="contact-icon" viewBox="0 0 14 14" aria-hidden="true">
          <circle cx="7" cy="7" r="7" fill="var(--magenta)"/>
          <circle cx="7" cy="7" r="4" fill="none" stroke="#fff" stroke-width="0.9"/>
          <ellipse cx="7" cy="7" rx="1.8" ry="4" fill="none" stroke="#fff" stroke-width="0.8"/>
          <line x1="3" y1="7" x2="11" y2="7" stroke="#fff" stroke-width="0.8"/>
        </svg>
        <span>lanternwayco.example</span>
      </li>
    </ul>

    <ul class="service-list">
      <li class="service-item service-strategy">Strategy</li>
      <li class="service-item service-analytics">Analytics</li>
      <li class="service-item service-branding">Branding</li>
      <li class="service-item service-research">Research</li>
    </ul>

    <div class="card-band"></div>
  </section>

</main>
</body>
</html>
```